Design required for boutique fire engineering firm in New Zealand

Our website was published based on free Wordpress templates, we'd like something a bit more bespoke, clean and simple.
Updates

Reason: didn't check this finished on a Sunday :)

Target Market(s)

architects, building owners, property developers

Industry/Entity Type

Boutique

Contact Information for Business Card

Logo
Fire Engineering

Desmond Harlow
Principal
+64 21 482 735
desmond@veltrane.nz
veltrane.nz

Number of Pages Required

3 page

Font styles to use
Sans Serif

Requirements
Nice to have
• On the business card, an embossed logo would be great - not sure if that's a design thing or just a print thing?
• Website, existing @ http://veltrane.nz for extent of content and general arrangement that I'm happy with.
• Ability to update the content with project bio's and some photos at a later date would be nice.

```html
<!DOCTYPE html>
<html lang="en">
<head>
<meta charset="utf-8">
<title>veltrane — Fire Engineering</title>
<link href="https://fonts.googleapis.com/css2?family=Montserrat:wght@300;400;500;600;700;800&display=swap" rel="stylesheet">
<style>
:root{
  --navy:#0b4a7e;
  --navy-deep:#083a63;
  --blue:#1b5e9e;
  --button:#2f6fb3;
  --cyan:#4fd5e2;
  --text:#6b6f75;
  --ink:#1d2a36;
  --line:#d9dde2;
  --icon-grey:#7d8895;
  --white:#ffffff;
}
*{box-sizing:border-box;margin:0;padding:0}
html,body{width:1200px;height:3593px;overflow:hidden}
body{position:relative;font-family:'Montserrat',sans-serif;color:var(--text);background:var(--white)}
.abs{position:absolute}
.btn{position:absolute;display:flex;align-items:center;justify-content:center;background:var(--button);color:var(--white);font-size:10px;font-weight:700;letter-spacing:.5px;border-radius:2px}
.section-title{position:absolute;left:0;width:1200px;text-align:center;font-size:34px;font-weight:800;color:var(--navy)}
.section-title.light{font-weight:400;color:var(--blue)}
.small{font-size:11px;line-height:18px}

/* header */
.site-header{top:0;left:0;width:1200px;height:60px;background:var(--white)}
.brand{display:flex;align-items:center;gap:8px;font-weight:700;color:var(--navy)}
.brand-dot{border-radius:50%;background:var(--navy)}
.main-nav{top:0;right:150px;height:60px;display:flex;align-items:center;gap:36px;font-size:11px;font-weight:700;color:var(--navy)}

/* hero */
.hero{top:60px;left:0;width:1200px;height:452px;background:linear-gradient(160deg,#c9d6e0 0%,#6c8aa4 30%,#2c4a66 60%,#1a2f45 100%)}
.hero-title{top:150px;left:0;width:1200px;text-align:center;color:var(--white);font-size:35px;font-weight:800;line-height:40px}
.hero-sub{top:245px;left:360px;width:480px;text-align:center;color:#e6edf3;font-size:11px;line-height:16px}
.dots{top:420px;left:578px;display:flex;gap:7px}
.dots span{width:9px;height:9px;border-radius:50%;background:#c7d2dc}
.dots span:first-child{background:var(--white);border:1px solid #889}

/* about */
.about{top:512px;left:0;width:1200px;height:413px;background:linear-gradient(90deg,#40cfe0,#5cdae6)}
.about-title{top:98px;left:150px;font-size:34px;font-weight:800;color:var(--white)}
.about-text{top:158px;left:150px;width:440px;color:#123c55;font-size:11px;line-height:18px}
.about-text p+p{margin-top:18px}
.about-image{top:15px;left:730px;width:230px;height:398px;background:linear-gradient(180deg,#dfeaf3,#3f6da3 60%,#1f3f72);border-radius:40px 40px 0 0}

/* services */
.service{position:absolute;top:1040px;width:300px;text-align:center}
.service-icon{width:120px;height:120px;margin:0 auto;border-radius:14px;background:linear-gradient(145deg,#dce8f4 0%,#8fb3d8 45%,#1f4f84 100%);box-shadow:inset 0 0 0 3px #1d3550}
.service h3{margin-top:22px;font-size:19px;font-weight:800;color:var(--blue)}
.service p{margin:10px auto 0;width:280px;font-size:10.5px;line-height:16px}
.service .btn{position:relative;margin:18px auto 0;width:105px;height:30px}

/* work */
.work{top:1375px;left:0;width:1200px;height:450px;background:var(--navy)}
.work .section-title{color:var(--white);top:50px}
.work-card{position:absolute;top:113px;width:316px}
.work-img{height:248px}
.work-card h4{margin-top:18px;color:var(--white);font-size:17px;font-weight:800}
.work-card span{display:block;margin-top:6px;color:#d3dde8;font-size:11px}
.arrow{top:228px}

/* blog */
.post{position:absolute;top:1930px;width:233px}
.post-img{height:190px}
.post-head{display:flex;gap:12px;margin-top:15px}
.date{flex:none;width:40px;height:42px;background:#f6e7a6;text-align:center;color:var(--ink);font-size:16px;font-weight:700;line-height:20px;padding-top:4px}
.date small{display:block;font-size:8px;font-weight:500;line-height:10px;color:var(--blue)}
.post-head h4{font-size:16px;font-weight:800;color:var(--blue);line-height:19px}
.post .by{margin-top:10px;font-size:10px}
.post .by b{font-weight:500;color:var(--ink)}
.post p{margin-top:14px;font-size:10px;line-height:16px}

/* team */
.member{position:absolute;top:2380px;width:300px;text-align:center}
.avatar{width:104px;height:104px;margin:0 auto;border-radius:50%;background:linear-gradient(180deg,#c3c9cf,#6b737c)}
.member h4{margin-top:20px;font-size:16px;font-weight:800;color:var(--blue)}
.member .role{margin-top:6px;font-size:9px;letter-spacing:.5px}
.member p{margin-top:8px;font-size:10px;line-height:15px}
.socials{display:flex;gap:8px;justify-content:center;margin-top:18px}
.socials span{display:flex;align-items:center;justify-content:center;width:30px;height:30px;border:1.5px solid var(--icon-grey);border-radius:50%;color:var(--icon-grey)}
.socials svg{width:14px;height:14px;fill:none;stroke:currentColor;stroke-width:1.6;stroke-linecap:round;stroke-linejoin:round}
.footer .socials span{border-color:var(--white);color:var(--white)}

/* testimonials */
.quote{position:absolute;top:2755px;display:flex;gap:18px}
.quote .avatar{width:104px;height:104px;margin:0;flex:none}
.quote p{width:340px;font-size:11px;line-height:17px;padding-top:4px}
.quote h5{margin-top:12px;font-size:11px;font-weight:700;color:var(--blue)}
.quote .org{font-size:8px;color:var(--text)}

/* contact */
.map{top:3005px;left:112px;width:480px;height:270px;background:linear-gradient(135deg,#eef0f2,#dde1e5)}
.field{position:absolute;left:608px;width:480px;height:30px;border:1px solid var(--line);font-size:10px;color:#a0a6ad;padding:9px 10px}

/* footer */
.footer{top:3343px;left:0;width:1200px;height:190px;background:var(--navy);color:var(--white)}
.footer h4{font-size:17px;font-weight:700}
.footer-bar{top:3533px;left:0;width:1200px;height:60px;background:var(--navy-deep);color:var(--white);font-size:10px}
.footer-links{right:150px;top:0;height:60px;display:flex;align-items:center;gap:30px;font-weight:700}
</style>
</head>
<body>

<header class="abs site-header">
  <div class="abs brand" style="left:150px;top:14px;font-size:24px"><span class="brand-dot" style="width:30px;height:30px"></span>veltrane</div>
  <nav class="abs main-nav"><span>ABOUT US</span><span>SERVICES</span><span>WORK</span><span>BLOG</span><span>OUR TEAM</span><span>CONTACT</span></nav>
</header>

<section class="abs hero" role="img" aria-label="Photograph looking up at glass office towers">
  <h1 class="abs hero-title">Architecture is a visual art, and<br>the buildings speak for themselves</h1>
  <p class="abs hero-sub">At vero eos et accusamus et iusto odio dignissimos ducimus qui blanditiis praesentium voluptatum deleniti atque corrupti quos dolores et quas molestias exceptur.</p>
  <div class="btn" style="left:552px;top:294px;width:100px;height:28px">GET STARTED</div>
  <div class="abs dots"><span></span><span></span><span></span></div>
</section>

<section class="abs about">
  <h2 class="abs about-title">About Us</h2>
  <div class="abs about-text">
    <p>veltrane is a boutique fire engineering firm based in Wellington, New Zealand, founded by Desmond Harlow in 2017. We provide consulting services in the built environment, including design and review services to assist in Building Consent applications, advice on property protection matters, observation of construction on site, and regulatory consultation.</p>
    <p>Desmond has worked as a fire engineer in New Zealand for over 20 years, having graduated from the University of Halloway with a Bachelor of Engineering with Honours and Masters of Engineering in Fire Engineering, and is a Chartered Professional Engineer.</p>
  </div>
  <div class="abs about-image" role="img" aria-label="Photograph of a curved glass high-rise tower"></div>
</section>

<h2 class="section-title" style="top:962px">Our Services</h2>
<div class="service" style="left:120px"><div class="service-icon" role="img" aria-label="Illustration of an engineer in a hard hat"></div><h3>DESIGN DEVELOPMENT</h3><p>At vero eos et accusamus et iusto odio dignissimos ducimus qui blanditiis praesentium voluptatum atque corrupti quos dolores et quas molestias.</p><div class="btn">LEARN MORE</div></div>
<div class="service" style="left:450px"><div class="service-icon" role="img" aria-label="Illustration of a surveying instrument on a tripod"></div><h3>MASTER PLANNING</h3><p>Vero eos et accusamus et iusto odio dignissimos ducimus qui blanditiis praesentium atque corrupti quos dolores et quas molestias excepturi.</p><div class="btn">LEARN MORE</div></div>
<div class="service" style="left:780px"><div class="service-icon" role="img" aria-label="Illustration of blueprints with a gear"></div><h3>DESIGN CONSULTATION</h3><p>Accusamus et iusto odio dignissimos ducimus qui blanditiis praesentium voluptatum atque corrupti quos dolores et quas molestias excepturi.</p><div class="btn">LEARN MORE</div></div>

<section class="abs work">
  <h2 class="section-title">Our Work</h2>
  <svg class="abs arrow" style="left:76px" width="18" height="30" viewBox="0 0 18 30"><path d="M15 3 4 15l11 12" fill="none" stroke="#fff" stroke-width="3"/></svg>
  <svg class="abs arrow" style="left:1106px" width="18" height="30" viewBox="0 0 18 30"><path d="M3 3l11 12L3 27" fill="none" stroke="#fff" stroke-width="3"/></svg>
  <div class="work-card" style="left:112px"><div class="work-img" role="img" aria-label="Photograph of a white stepped building facade" style="background:linear-gradient(135deg,#e4e8ec,#a9b2ba)"></div><h4>Perspiciatis Unde Omnis</h4><span>Accusamus, Iusto odio, Dignissimos</span></div>
  <div class="work-card" style="left:443px"><div class="work-img" role="img" aria-label="Photograph of angular green glass roofs" style="background:linear-gradient(135deg,#cfe0dc,#3f7a6c 55%,#1f3f3a)"></div><h4>Sed Ut Unde Omnis</h4><span>Vero eos, Ducimus</span></div>
  <div class="work-card" style="left:773px"><div class="work-img" role="img" aria-label="Photograph of a pink and white building front" style="background:linear-gradient(180deg,#a9d4ea,#e8a2b8 45%,#d27a98)"></div><h4>Iste Natus Error</h4><span>Sed ut, Perspiciatis</span></div>
</section>

<h2 class="section-title" style="top:1868px">Our Blog</h2>
<div class="post" style="left:112px"><div class="post-img" role="img" aria-label="Photograph of a city skyline with curved architecture" style="background:linear-gradient(180deg,#c9dbe6,#6f8f78)"></div><div class="post-head"><div class="date">19<small>APR</small></div><h4>Perspiciatis Unde Omnis</h4></div><div class="by">by <b>admin</b></div><p>Nemo enim ipsam voluptatem quia voluptas sit aspernatur aut odit aut fugit.</p></div>
<div class="post" style="left:360px"><div class="post-img" role="img" aria-label="Photograph of downtown towers at sunset" style="background:linear-gradient(180deg,#9fc3e0,#5a6f86 70%,#c49a6c)"></div><div class="post-head"><div class="date">18<small>APR</small></div><h4>Quia voluptas sit aspernatur aut</h4></div><div class="by">by <b>admin</b></div><p>Nemo enim ipsam voluptatem quia voluptas sit aspernatur aut odit aut fugit.</p></div>
<div class="post" style="left:608px"><div class="post-img" role="img" aria-label="Photograph of a glass tower against blue sky" style="background:linear-gradient(160deg,#dfeaf4,#4f7fb0 60%,#2d4f78)"></div><div class="post-head"><div class="date">17<small>APR</small></div><h4>Perspiciatis Unde Omnis</h4></div><div class="by">by <b>admin</b></div><p>Nemo enim ipsam voluptatem quia voluptas sit aspernatur aut odit aut fugit.</p></div>
<div class="post" style="left:856px"><div class="post-img" role="img" aria-label="Photograph of a red brick corner building" style="background:linear-gradient(180deg,#cfe3f2,#b8654f 60%,#7c3e32)"></div><div class="post-head"><div class="date">16<small>APR</small></div><h4>Quia voluptas sit aspernatur</h4></div><div class="by">by <b>admin</b></div><p>Nemo enim ipsam voluptatem quia voluptas sit aspernatur aut odit aut fugit.</p></div>

<h2 class="section-title" style="top:2312px">Our Team</h2>
<div class="member" style="left:120px"><div class="avatar" role="img" aria-label="Portrait photograph of a team member"></div><h4>Rowan Castell</h4><div class="role">FOUNDER</div><p>Vero eos et accusamus et iusto odio dignissimos ducimus qui blanditiis praesentium voluptatum atque.</p>
  <div class="socials">
    <span><svg viewBox="0 0 14 14"><path d="M6 8.2a2.6 2.6 0 0 0 3.7 0l2-2a2.6 2.6 0 0 0-3.7-3.7l-.9.9"/><path d="M8 5.8a2.6 2.6 0 0 0-3.7 0l-2 2a2.6 2.6 0 0 0 3.7 3.7l.9-.9"/></svg></span>
    <span><svg viewBox="0 0 14 14"><rect x="1.5" y="3" width="11" height="8"/><path d="M1.5 3l5.5 4.5L12.5 3"/></svg></span>
    <span><svg viewBox="0 0 14 14"><circle cx="7" cy="7" r="5.5"/><path d="M1.5 7h11M7 1.5c2 2 2 9 0 11M7 1.5c-2 2-2 9 0 11"/></svg></span>
  </div></div>
<div class="member" style="left:450px"><div class="avatar" role="img" aria-label="Portrait photograph of a team member"></div><h4>Miles Ardent</h4><div class="role">FOUNDER</div><p>Eos et accusamus et iusto odio dignissimos ducimus qui blanditiis praesentium voluptatum atque corrupti quos.</p>
  <div class="socials">
    <span><svg viewBox="0 0 14 14"><path d="M6 8.2a2.6 2.6 0 0 0 3.7 0l2-2a2.6 2.6 0 0 0-3.7-3.7l-.9.9"/><path d="M8 5.8a2.6 2.6 0 0 0-3.7 0l-2 2a2.6 2.6 0 0 0 3.7 3.7l.9-.9"/></svg></span>
    <span><svg viewBox="0 0 14 14"><rect x="1.5" y="3" width="11" height="8"/><path d="M1.5 3l5.5 4.5L12.5 3"/></svg></span>
    <span><svg viewBox="0 0 14 14"><circle cx="7" cy="7" r="5.5"/><path d="M1.5 7h11M7 1.5c2 2 2 9 0 11M7 1.5c-2 2-2 9 0 11"/></svg></span>
  </div></div>
<div class="member" style="left:780px"><div class="avatar" role="img" aria-label="Portrait photograph of a team member"></div><h4>Tessa Marlow</h4><div class="role">FOUNDER</div><p>Et accusamus et iusto odio dignissimos ducimus qui blanditiis praesentium voluptatum atque corrupti quos.</p>
  <div class="socials">
    <span><svg viewBox="0 0 14 14"><path d="M6 8.2a2.6 2.6 0 0 0 3.7 0l2-2a2.6 2.6 0 0 0-3.7-3.7l-.9.9"/><path d="M8 5.8a2.6 2.6 0 0 0-3.7 0l-2 2a2.6 2.6 0 0 0 3.7 3.7l.9-.9"/></svg></span>
    <span><svg viewBox="0 0 14 14"><rect x="1.5" y="3" width="11" height="8"/><path d="M1.5 3l5.5 4.5L12.5 3"/></svg></span>
    <span><svg viewBox="0 0 14 14"><circle cx="7" cy="7" r="5.5"/><path d="M1.5 7h11M7 1.5c2 2 2 9 0 11M7 1.5c-2 2-2 9 0 11"/></svg></span>
  </div></div>

<h2 class="section-title light" style="top:2688px">Let's see what our client said</h2>
<div class="quote" style="left:112px"><div class="avatar" role="img" aria-label="Portrait photograph of a client"></div><div><p>"Sed ut perspiciatis unde omnis iste natus error sit voluptatem accusantium doloremque laudantium, totam rem aperiam, eaque ipsa quae ab illo inventore"</p><h5>Elliot Vane</h5><div class="org">NORTHBAY</div></div></div>
<div class="quote" style="left:608px"><div class="avatar" role="img" aria-label="Portrait photograph of a client"></div><div><p>"Sed ut perspiciatis unde omnis iste natus error sit voluptatem accusantium doloremque laudantium, totam rem aperiam, eaque ipsa quae ab illo inventore"</p><h5>Jonah Pryce</h5><div class="org">KESTRELL</div></div></div>

<h2 class="section-title light" style="top:2932px">Connet with us</h2>
<div class="abs map" role="img" aria-label="Street map showing the office location">
  <svg class="abs" style="left:226px;top:110px" width="30" height="44" viewBox="0 0 30 44"><path d="M15 0C6.7 0 0 6.7 0 15c0 11 15 29 15 29s15-18 15-29C30 6.7 23.3 0 15 0z" fill="#2f6fb3"/><circle cx="15" cy="15" r="6" fill="#fff"/></svg>
</div>
<div class="field" style="top:3005px">Your Name</div>
<div class="field" style="top:3050px">Your email</div>
<div class="field" style="top:3095px">Subject</div>
<div class="field" style="top:3140px;height:88px">Message</div>
<div class="btn" style="left:608px;top:3246px;width:96px;height:30px">CONTACT</div>

<footer class="abs footer">
  <div class="abs brand" style="left:185px;top:32px;font-size:26px;color:#fff"><span class="brand-dot" style="width:30px;height:30px;background:#fff"></span>veltrane</div>
  <div class="abs" style="left:155px;top:92px;width:230px;height:28px;background:#fff;color:#9aa;font-size:9px;padding:9px 8px">Your email</div>
  <div class="btn" style="left:218px;top:136px;width:102px;height:28px;background:#5b6f86">SUBSCRIBE</div>
  <h4 class="abs" style="left:0;width:1200px;text-align:center;top:38px">About</h4>
  <p class="abs small" style="left:445px;width:310px;top:70px;text-align:center;color:#d6e1ec;font-size:10px;line-height:15px">Eos et accusamus et iusto odio dignissimos ducimus qui blanditiis praesentium voluptatum deleniti atque. At vero eos et accusamus iusto odio dignissimos.</p>
  <div class="btn" style="left:550px;top:136px;width:100px;height:28px">GET QUOTE</div>
  <h4 class="abs" style="left:880px;top:28px">Contact Us</h4>
  <div class="abs" style="left:880px;top:78px;font-size:10px;display:flex;align-items:center;gap:8px"><svg width="13" height="10" viewBox="0 0 13 10"><rect x=".5" y=".5" width="12" height="9" fill="none" stroke="#fff"/><path d="M.5.5l6 5 6-5" fill="none" stroke="#fff"/></svg>INFO@VELTRANE.NZ</div>
  <div class="abs" style="left:880px;top:100px;font-size:10px;display:flex;align-items:center;gap:8px"><svg width="12" height="12" viewBox="0 0 12 12"><path d="M3 1l2 3-1.3 1.3a7 7 0 0 0 3 3L8 7l3 2-1 2C5 11 1 7 1 2z" fill="#fff"/></svg>+64 21 482 735</div>
  <div class="abs socials" style="left:880px;top:128px;margin:0">
    <span><svg viewBox="0 0 14 14"><path d="M6 8.2a2.6 2.6 0 0 0 3.7 0l2-2a2.6 2.6 0 0 0-3.7-3.7l-.9.9"/><path d="M8 5.8a2.6 2.6 0 0 0-3.7 0l-2 2a2.6 2.6 0 0 0 3.7 3.7l.9-.9"/></svg></span>
    <span><svg viewBox="0 0 14 14"><rect x="1.5" y="3" width="11" height="8"/><path d="M1.5 3l5.5 4.5L12.5 3"/></svg></span>
    <span><svg viewBox="0 0 14 14"><circle cx="7" cy="7" r="5.5"/><path d="M1.5 7h11M7 1.5c2 2 2 9 0 11M7 1.5c-2 2-2 9 0 11"/></svg></span>
  </div>
</footer>
<div class="abs footer-bar">
  <div class="abs" style="left:112px;top:24px">© veltrane | 2017</div>
  <nav class="abs footer-links"><span>HOME</span><span>SERVICE</span><span>ABOUT</span><span>BLOG</span><span>CONTACT</span></nav>
</div>

</body>
</html>
```